Business Card Design

I am starting my therapy private practice. I will be an in home therapist, so I go into family's homes instead of using an office to do family/marriage therapy. Therefore, I do not have an office address. I am looking for something in the black, red, gray, and blue color scheme that appeals to both families, couples and teenagers.

Industry/Entity Type

Business

Contact Information for Business Card

Lena Brovick, MS, MFT Intern
Marriage and Family Therapy
In Home Therapist
508-241-6039
Lena@LenaBrovick.net

```html
<!DOCTYPE html>
<html lang="en">
<head>
<meta charset="utf-8">
<title>Lena Brovick – Business Card</title>
<link href="https://fonts.googleapis.com/css2?family=Open+Sans:wght@400;600;700&display=swap" rel="stylesheet">
<style>
  :root {
    --bg-light: #f4f4f4;
    --bg-dark: #cfcfcf;
    --card: #f7f7f7;
    --ink: #1f1f1f;
    --red: #e8262a;
    --blue: #2f95dc;
    --gray: #8e8e8e;
    --text-gray: #555555;
  }
  * { margin: 0; padding: 0; box-sizing: border-box; }
  html, body {
    width: 1200px;
    height: 1200px;
    overflow: hidden;
  }
  body {
    background: radial-gradient(circle at 40% 40%, var(--bg-light), var(--bg-dark));
    font-family: "Open Sans", Arial, sans-serif;
    display: flex;
    align-items: center;
    justify-content: center;
  }
  .business-card {
    position: relative;
    width: 1000px;
    height: 572px;
    background: var(--card);
    box-shadow: 0 18px 40px rgba(0,0,0,0.18);
    overflow: hidden;
  }
  .brand-square {
    position: absolute;
    left: 0;
    top: 150px;
    width: 62px;
    height: 38px;
    background: var(--ink);
  }
  .brand-name {
    position: absolute;
    left: 86px;
    top: 128px;
    font-size: 64px;
    font-weight: 700;
    color: var(--red);
    letter-spacing: 2px;
    line-height: 1;
  }
  .title-bar {
    position: absolute;
    left: 415px;
    right: 0;
    top: 232px;
    height: 54px;
    background: var(--ink);
    color: #ffffff;
    font-size: 27px;
    font-weight: 400;
    display: flex;
    align-items: center;
    padding-left: 22px;
  }
  .holder {
    position: absolute;
    left: 370px;
    top: 300px;
  }
  .holder-name {
    font-size: 32px;
    font-weight: 700;
    color: var(--blue);
    line-height: 1.2;
  }
  .holder-role {
    font-size: 25px;
    color: var(--text-gray);
    line-height: 1.2;
  }
  .contact-list {
    position: absolute;
    left: 340px;
    top: 395px;
    list-style: none;
    font-size: 26px;
    color: var(--text-gray);
  }
  .contact-item {
    display: flex;
    align-items: center;
    gap: 10px;
    line-height: 1.45;
  }
  .contact-icon {
    width: 22px;
    height: 22px;
    flex: none;
  }
  .accent-stripe {
    position: absolute;
    left: 0;
    right: 0;
    bottom: 0;
    height: 14px;
    display: flex;
  }
  .stripe-red { width: 30%; background: var(--red); }
  .stripe-blue { width: 40%; background: var(--blue); }
  .stripe-gray { width: 30%; background: var(--gray); }
</style>
</head>
<body>
  <article class="business-card">
    <div class="brand-square"></div>
    <div class="brand-name">BROVICK</div>

    <div class="title-bar">Intern Marriage and Family Therapy</div>

    <div class="holder">
      <p class="holder-name">Lena Brovick, MS</p>
      <p class="holder-role">Home Therapist</p>
    </div>

    <ul class="contact-list">
      <li class="contact-item">
        <svg class="contact-icon" viewBox="0 0 22 22" aria-hidden="true">
          <circle cx="11" cy="11" r="11" fill="#3a3a3a"/>
          <path d="M7 6h3v3l-1.5 1a6 6 0 0 0 3.5 3.5l1-1.5h3v3h-1.5A8 8 0 0 1 7 7.5z" fill="#ffffff"/>
        </svg>
        <span>508-241-6039</span>
      </li>
      <li class="contact-item">
        <svg class="contact-icon" viewBox="0 0 22 22" aria-hidden="true">
          <circle cx="11" cy="11" r="11" fill="#3a3a3a"/>
          <rect x="5" y="7" width="12" height="8" fill="none" stroke="#ffffff" stroke-width="1.4"/>
          <path d="M5 7l6 5 6-5" fill="none" stroke="#ffffff" stroke-width="1.4"/>
        </svg>
        <span>Lena@LenaBrovick.net</span>
      </li>
    </ul>

    <div class="accent-stripe">
      <span class="stripe-red"></span>
      <span class="stripe-blue"></span>
      <span class="stripe-gray"></span>
    </div>
  </article>
</body>
</html>
```